SkyvornQ Business Cards and Stationary Design

Need a design for our business cards and stationary. I want to carry on the theme of the logo. I want the business cards to have a design on the back. I would like the business cards and the stationary to carry the same theme, design scheme, and branding

Target Market(s)

Airlines and Maintenance Facilities

Industry/Entity Type

Aviation

Contact Information for Business Card

Address: 4827 Tallowmere Lane, Fort Pierce, Florida, 34951

Font styles to use
Serif
Sans Serif

Colors

Designer to choose colors to be used in the design.

```html
<!DOCTYPE html>
<html lang="en">
<head>
<meta charset="utf-8">
<title>SkyvornQ Business Card</title>
<link rel="stylesheet" href="https://fonts.googleapis.com/css2?family=Roboto+Slab:wght@400;700&family=Fira+Sans:wght@400&display=swap">
<style>
  :root {
    --navy-deep: #061c45;
    --navy-mid: #0c2c63;
    --navy-light: #1d4488;
    --wing-tone: #123770;
    --wing-shade: #071a40;
    --text-white: #ffffff;
  }
  html, body {
    margin: 0;
    padding: 0;
    width: 1200px;
    height: 716px;
    overflow: hidden;
    background: var(--navy-deep);
  }
  .business-card {
    position: relative;
    width: 1200px;
    height: 716px;
    overflow: hidden;
    background: linear-gradient(180deg, var(--navy-deep) 0%, var(--navy-mid) 45%, var(--navy-deep) 100%);
  }
  .wing-photo {
    position: absolute;
    inset: 0;
    width: 1200px;
    height: 716px;
  }
  .aircraft-drawing {
    position: absolute;
    left: 560px;
    top: 285px;
    width: 570px;
    height: 300px;
    border-radius: 18px;
    background: radial-gradient(ellipse at 50% 50%, rgba(255, 255, 255, 0.16) 0%, rgba(255, 255, 255, 0.06) 60%, rgba(255, 255, 255, 0.03) 100%);
    border: 1px solid rgba(255, 255, 255, 0.18);
  }
  .card-text {
    position: absolute;
    left: 137px;
    top: 0;
    color: var(--text-white);
  }
  .holder-name {
    position: absolute;
    left: 0;
    top: 116px;
    margin: 0;
    font-family: "Roboto Slab", Georgia, serif;
    font-weight: 700;
    font-size: 52px;
    letter-spacing: 2px;
    line-height: 1;
    white-space: nowrap;
  }
  .holder-title {
    position: absolute;
    left: 0;
    top: 202px;
    margin: 0;
    font-family: "Fira Sans", Arial, sans-serif;
    font-size: 36px;
    line-height: 1;
    white-space: nowrap;
  }
  .contact-list {
    position: absolute;
    left: 0;
    top: 338px;
    margin: 0;
    padding: 0;
    list-style: none;
    font-family: "Roboto Slab", Georgia, serif;
    font-size: 36px;
    line-height: 55.5px;
    letter-spacing: 0.5px;
    white-space: nowrap;
  }
</style>
</head>
<body>
  <main class="business-card">
    <svg class="wing-photo" viewBox="0 0 1200 716" role="img" aria-label="Photograph of an airliner wing seen from a cabin window, tinted deep navy blue">
      <defs>
        <linearGradient id="wing-gradient" x1="0" y1="0" x2="1" y2="1">
          <stop offset="0" stop-color="#0a2557"/>
          <stop offset="0.5" stop-color="#123770"/>
          <stop offset="1" stop-color="#0a2557"/>
        </linearGradient>
        <linearGradient id="wing-shadow" x1="0" y1="0" x2="1" y2="0">
          <stop offset="0" stop-color="#071a40" stop-opacity="0"/>
          <stop offset="0.5" stop-color="#071a40" stop-opacity="0.7"/>
          <stop offset="1" stop-color="#071a40" stop-opacity="0.9"/>
        </linearGradient>
      </defs>
      <rect x="0" y="0" width="1200" height="716" fill="transparent"/>
      <polygon points="70,78 1200,230 1200,370 820,300 260,190 180,150" fill="url(#wing-gradient)"/>
      <polygon points="400,250 1200,400 1200,560 820,480 460,300" fill="url(#wing-shadow)"/>
    </svg>
    <div class="aircraft-drawing" role="img" aria-label="White line drawing of a jet airliner seen head-on in a banking turn"></div>
    <section class="card-text">
      <h1 class="holder-name">NAME HERE</h1>
      <p class="holder-title">Title</p>
      <ul class="contact-list">
        <li>Office Number</li>
        <li>Mobile Number</li>
        <li>Email</li>
        <li>Website</li>
        <li>4827 Tallowmere Lane,</li>
        <li>Fort Pierce, Florida, 34951</li>
      </ul>
    </section>
  </main>
</body>
</html>
```